Etiketten für Dips
Zielgruppe
Landwirtschaft mit Direktvermarktung und Diversifikation durch workshops und Beratung zur Selbstversorgung
Zielgruppe: LOHAS, Best Agers
Aufgabenstellung
es gibt pikante und süße Dips (Weiters Salz und Essig) unter dem Motto 'Würzen | Dippen | Toppen' (das soll unbedingt überall mit drauf aufs Etikett), Etikett passend zum Logo - möglicherweise Teile davon auch am Etikett? durchscheinend aber farbig? die Etiketten jeweils in unterschiedlichen 'Farbmotto' so dass eine bunte aber gediegene Serie mit Wiedererkennung entstehen die höheres Preissegment gerecht wird/unterstreicht. Etikett soll nur 1 Teil sein, da am Deckel der Gläser ohnehin das Logoetikett drauf kommt. Bei Siegerprojekt gerne weitere Zusammenarbeit für die weiteren Etiketten.
Produkte für die Etiketten benötigt werden: Mara Bunt (Tomaten-Dip), Brisa Paul (Salz mit Tomaten), Sommer-Rübli (Grillsauce/-dip), Moosgeflüster (Lebkuchenmarmelade), Wild Mango, Kornbrise (Gewürzessig mit Chilli)
Bitte an alle notwendigen Inhalte eines Lebensmitteletiketts denken bzw Platzhalter einfügen

```html
<!DOCTYPE html>
<html lang="de">
<head>
<meta charset="utf-8">
<title>Mara Bunt – Tomaten-Dip Etikett</title>
<link rel="stylesheet" href="https://fonts.googleapis.com/css2?family=Source+Sans+3:wght@400;600&family=Kalam:wght@400;700&display=swap">
<style>
  :root {
    --page-bg: #c2c2c2;
    --label-pink: #ef6a78;
    --ring-rose: #e8344c;
    --ring-red: #e2001c;
    --oval-grey: #c9c9cb;
    --vine-green: #a9c99a;
    --ink: #1e1a1b;
    --ink-soft: #3a2427;
    --title-red: #e5001b;
    --white: #ffffff;
  }
  * { margin: 0; padding: 0; box-sizing: border-box; }
  html, body {
    width: 1200px; height: 816px; overflow: hidden;
    background: var(--page-bg);
  }
  .label {
    position: absolute; left: 30px; top: 241px;
    width: 1140px; height: 334px; overflow: hidden;
    background: var(--label-pink);
    font-family: "Source Sans 3", "Myriad Pro", sans-serif;
    color: var(--ink-soft);
  }
  .label-shapes { position: absolute; inset: 0; }
  .copy {
    position: absolute; font-size: 14px; line-height: 20px; letter-spacing: -0.2px;
  }
  .copy p + p { margin-top: 19px; }
  .copy-left { left: 16px; top: 46px; width: 250px; }
  .copy-right { left: 895px; top: 88px; width: 245px; }
  .contents-heading {
    position: absolute; left: 896px; top: 10px;
    font-size: 29px; font-weight: 400; color: var(--white);
  }
  .best-before {
    position: absolute; left: 19px; top: 274px; font-size: 14px;
  }
  .best-before-field {
    position: absolute; left: 15px; top: 298px; width: 259px; height: 25px;
    background: var(--white); border: 2px solid var(--ink);
  }
  .product-name {
    position: absolute; left: 471px; top: 110px; width: 220px; text-align: center;
    font-family: "Kalam", cursive; font-weight: 700; font-size: 42px; line-height: 48px;
    color: var(--title-red);
  }
  .product-type {
    position: absolute; left: 471px; top: 155px; width: 220px; text-align: center;
    font-family: "Kalam", cursive; font-weight: 700; font-size: 29px; line-height: 34px;
    color: var(--ink);
  }
  .motto span {
    position: absolute; font-family: "Kalam", cursive; font-size: 29px; line-height: 34px;
    color: var(--ink);
  }
  .motto .m1 { left: 433px; top: 222px; }
  .motto .m2 { left: 518px; top: 255px; }
  .motto .m3 { left: 603px; top: 284px; }
</style>
</head>
<body>
  <section class="label">
    <svg class="label-shapes" viewBox="0 0 1140 334" width="1140" height="334">
      <ellipse cx="568" cy="180" rx="340" ry="260" fill="var(--ring-rose)"/>
      <ellipse cx="568" cy="180" rx="318" ry="250" fill="var(--ring-red)"/>
      <ellipse cx="568" cy="180" rx="283" ry="236" fill="var(--oval-grey)"/>
      <ellipse class="vine-illustration" role="img"
        aria-label="Gezeichnete Ranke mit Tomate, Paprika, Erdbeere, Karotte und Blättern"
        cx="568" cy="190" rx="215" ry="165" fill="none"
        stroke="var(--vine-green)" stroke-width="40" opacity="0.7"/>
    </svg>

    <div class="copy copy-left">
      <p>Lorem ipsum dolor sit amet,<br>consetetur sadipscing elitr,<br>sed diam nonumy eirmod tempor<br>invidunt ut labore et dolore magna<br>aliquyam erat, sed diam voluptua.</p>
      <p>At vero eos et accusam et justo<br>&nbsp;duo dolores et ea rebum.<br>Stet clita kasd gubergren,</p>
    </div>
    <div class="best-before">Haltbar bis:</div>
    <div class="best-before-field"></div>

    <h1 class="product-name">Mara Bunt</h1>
    <h2 class="product-type">Tomaten-Dip</h2>
    <div class="motto">
      <span class="m1">Würzen</span>
      <span class="m2">Dippen</span>
      <span class="m3">Toppen</span>
    </div>

    <h3 class="contents-heading">Inhaltsangabe</h3>
    <div class="copy copy-right">
      <p>Lorem ipsum dolor sit amet,<br>consetetur sadipscing elitr,<br>sed diam nonumy eirmod tempor<br>invidunt ut labore et dolore magna<br>aliquyam erat, sed diam voluptua.</p>
      <p>At vero eos et accusam et justo<br>&nbsp;duo dolores et ea rebum.<br>Stet clita kasd gubergren,</p>
    </div>
  </section>
</body>
</html>
```